Dune Air & Plus business card

I need an awesome, double-sided business card designed with our new logo. I would like the one side black with the colored logo, and the back side is all yours. I'd like to see horizontal and vertical layouts. Get creative! Thank you.

Target Market(s)

HVAC, Heating and Cooling in Phoenix, AZ

Industry/Entity Type

HVAC

Contact Information for Business Card

We need our new logo on the card. Tom Harker, (623) 555-0142, tom@trydunesair.com, www.trydunesair.com, ROC 514273

```html
<!DOCTYPE html>
<html lang="en">
<head>
<meta charset="utf-8">
<title>Dune Air &amp; Plus — Business Card</title>
<link href="https://fonts.googleapis.com/css2?family=Quicksand:wght@500;600;700&display=swap" rel="stylesheet">
<style>
  :root {
    --page-bg: #e9e9ec;
    --card-dark: #2d2d2f;
    --brand-blue: #0a6fc2;
    --brand-orange: #f07a22;
    --brand-red: #d93a22;
    --door-grey: #b8b8b8;
    --text-light: #ffffff;
    --text-muted: #a9a9ad;
  }
  * { margin: 0; padding: 0; box-sizing: border-box; }
  html, body {
    width: 1200px; height: 874px; overflow: hidden;
    background: var(--page-bg);
    font-family: "Quicksand", sans-serif;
  }
  .canvas { position: relative; width: 1200px; height: 874px; }

  .card {
    position: absolute; left: 320px; width: 560px; height: 320px;
    border-radius: 18px; overflow: hidden;
    box-shadow: 0 10px 30px rgba(0,0,0,.18);
  }

  /* Back side */
  .card--back { top: 70px; background: var(--card-dark); }
  .brand-lockup {
    position: absolute; left: 0; right: 0; top: 118px;
    display: flex; align-items: center; justify-content: center; gap: 14px;
  }
  .brand-lockup__dot {
    width: 22px; height: 22px; border-radius: 50%; background: var(--brand-orange);
  }
  .brand-lockup__name {
    font-weight: 700; font-size: 40px; color: var(--brand-blue); letter-spacing: .5px;
  }
  .back-web {
    position: absolute; left: 0; right: 0; top: 262px; text-align: center;
    font-size: 15px; letter-spacing: 3px; color: var(--text-muted); font-weight: 600;
  }
  .back-web__domain { color: var(--brand-red); }

  /* Front side */
  .card--front { top: 470px; background: #fff; }
  .card__art { position: absolute; inset: 0; }
  .holder-name {
    position: absolute; left: 150px; top: 72px;
    font-size: 28px; font-weight: 600; color: var(--text-light); letter-spacing: .5px;
  }
  .contact-list {
    position: absolute; left: 318px; top: 110px; list-style: none;
    color: var(--text-light); font-size: 17px; font-weight: 600;
  }
  .contact-list li { display: flex; align-items: center; gap: 10px; line-height: 24px; }
  .contact-list svg { width: 13px; height: 13px; flex: none; fill: var(--text-light); }
</style>
</head>
<body>
<main class="canvas">

  <section class="card card--back" aria-label="Business card back">
    <div class="brand-lockup">
      <span class="brand-lockup__dot"></span>
      <span class="brand-lockup__name">Dune Air &amp; Plus</span>
    </div>
    <p class="back-web">www.<span class="back-web__domain">trydunesair</span>.com</p>
  </section>

  <section class="card card--front" aria-label="Business card front">
    <svg class="card__art" viewBox="0 0 560 320" preserveAspectRatio="none">
      <defs>
        <linearGradient id="warmPanel" x1="1" y1="0" x2="0.4" y2="1">
          <stop offset="0" stop-color="#d6301f"/>
          <stop offset="1" stop-color="#f07a22"/>
        </linearGradient>
        <linearGradient id="garageArt" x1="0" y1="0" x2="0" y2="1">
          <stop offset="0" stop-color="#0a6fc2"/>
          <stop offset="1" stop-color="#c9ccd2"/>
        </linearGradient>
      </defs>
      <polygon points="0,0 270,0 262,190 0,190" fill="var(--brand-blue)"/>
      <polygon points="270,0 560,0 560,320 470,320 262,190" fill="url(#warmPanel)"/>
      <polygon role="img" aria-label="Illustration of a garage building with three roll-up doors"
               points="0,190 262,190 470,320 0,320" fill="url(#garageArt)"/>
    </svg>

    <h1 class="holder-name">TOM HARKER</h1>

    <ul class="contact-list">
      <li>
        <svg viewBox="0 0 24 24" aria-hidden="true"><path d="M6.6 10.8a15.1 15.1 0 0 0 6.6 6.6l2.2-2.2c.3-.3.7-.4 1-.2 1.1.4 2.3.6 3.6.6.6 0 1 .4 1 1V20c0 .6-.4 1-1 1A17 17 0 0 1 3 4c0-.6.4-1 1-1h3.5c.6 0 1 .4 1 1 0 1.3.2 2.5.6 3.6.1.3 0 .7-.2 1z"/></svg>
        (623) 555-0142
      </li>
      <li>
        <svg viewBox="0 0 24 24" aria-hidden="true"><path d="M2 5h20v14H2zm2 2v.5l8 5 8-5V7l-8 5z"/></svg>
        tom@trydunesair.com
      </li>
      <li>
        <svg viewBox="0 0 24 24" aria-hidden="true"><circle cx="12" cy="12" r="10"/></svg>
        www.trydunesair.com
      </li>
    </ul>
  </section>

</main>
</body>
</html>
```